Market Research firm needs updated business cards with new logo

We need the logo to be included somewhere on the card (attached). We would also like the phrases "Independent, Objective, Comprehensive" and "Research You Can Trust" somewhere on the card. Front or back. Our colors are hex codes 6075a7, e48d25 and 5a5b5b. Though you are certainly not limited to those shades, whatever you produce should coordinate with them. I have also attached our favicon. Feel free to use it in your design, but please do not use it to replace the full logo.

Contact Information for Business Card

see project description

Other font styles liked:
• Open Sans

Requirements
Must have
• the logo
• We use Open Sans font

```html
<!DOCTYPE html>
<html lang="en">
<head>
<meta charset="utf-8">
<title>Northmark Research – Business Card</title>
<link rel="stylesheet" href="https://fonts.googleapis.com/css2?family=Montserrat:wght@300;400;500;600;700&display=swap">
<style>
  :root {
    --canvas-bg: #d9dcdf;
    --front-dark: #5d7d8f;
    --front-light: #93b3c1;
    --accent-orange: #f0931f;
    --text-grey: #5a5b5b;
    --logo-grey: #7d8790;
    --card-white: #ffffff;
    --white: #ffffff;
  }
  * { box-sizing: border-box; margin: 0; padding: 0; }
  html, body {
    width: 1200px; height: 900px; overflow: hidden;
    background: var(--canvas-bg);
    font-family: "Montserrat", sans-serif;
  }
  .sheet {
    width: 1200px; height: 900px;
    display: flex; flex-direction: column;
    align-items: center; justify-content: center; gap: 56px;
  }
  .card {
    width: 600px; height: 343px;
    position: relative; overflow: hidden;
    box-shadow: 0 10px 28px rgba(0,0,0,0.18);
  }
  /* Front */
  .card-front {
    background: linear-gradient(135deg, var(--front-dark) 0%, var(--front-light) 100%);
    color: var(--white);
  }
  .brand {
    display: flex; align-items: center; gap: 12px; white-space: nowrap;
  }
  .brand-dot {
    width: 16px; height: 16px; border-radius: 50%;
    background: var(--accent-orange); flex: none;
  }
  .card-front .brand {
    position: absolute; left: 72px; top: 96px;
  }
  .card-front .brand-name {
    font-size: 42px; font-weight: 300; letter-spacing: -0.5px; color: var(--white);
  }
  .taglines { position: absolute; left: 100px; top: 196px; white-space: nowrap; }
  .tagline-values {
    font-size: 15px; font-weight: 400; letter-spacing: 0.6px; color: var(--white);
  }
  .tagline-promise {
    margin-top: 10px; font-size: 17px; font-weight: 600; letter-spacing: 0.4px;
    color: var(--accent-orange);
  }
  /* Back */
  .card-back { background: var(--card-white); }
  .card-back .brand {
    position: absolute; left: 36px; top: 156px; gap: 8px;
  }
  .card-back .brand-dot { width: 10px; height: 10px; }
  .card-back .brand-name {
    font-size: 21px; font-weight: 400; letter-spacing: -0.3px; color: var(--logo-grey);
  }
  .contact {
    position: absolute; left: 328px; top: 92px;
    color: var(--text-grey); white-space: nowrap;
  }
  .contact-name {
    font-size: 22px; font-weight: 600; color: var(--accent-orange); letter-spacing: 0.5px;
  }
  .contact-title { font-size: 15px; font-weight: 500; margin-top: 1px; letter-spacing: 0.4px; }
  .contact-address {
    margin-top: 18px; font-size: 12px; line-height: 19px; letter-spacing: 0.3px;
  }
  .contact-lines { margin-top: 16px; list-style: none; }
  .contact-lines li {
    display: flex; align-items: center; gap: 9px;
    font-size: 12px; line-height: 22px; letter-spacing: 0.2px;
  }
  .contact-lines svg { width: 12px; height: 12px; flex: none; }
</style>
</head>
<body>
<main class="sheet">
  <section class="card card-front" aria-label="Card front">
    <div class="brand">
      <span class="brand-dot"></span>
      <span class="brand-name">Northmark Research</span>
    </div>
    <div class="taglines">
      <p class="tagline-values">Independent, Objective, Comprehensive</p>
      <p class="tagline-promise">Research You Can Trust</p>
    </div>
  </section>

  <section class="card card-back" aria-label="Card back">
    <div class="brand">
      <span class="brand-dot"></span>
      <span class="brand-name">Northmark Research</span>
    </div>
    <div class="contact">
      <p class="contact-name">John Doe</p>
      <p class="contact-title">Manager</p>
      <p class="contact-address">48 Alder Lane<br>Brookfield, AB, T2X 4K7</p>
      <ul class="contact-lines">
        <li>
          <svg viewBox="0 0 12 12" aria-hidden="true"><path d="M3 1 L5 3.5 L4 5 Q5 7 7 8 L8.5 7 L11 9 L9.5 11 Q5 11 1 6 Q1 2.5 3 1Z" fill="var(--accent-orange)"/></svg>
          <span>555-014-2368</span>
        </li>
        <li>
          <svg viewBox="0 0 12 12" aria-hidden="true"><rect x="0.5" y="2" width="11" height="8" fill="var(--accent-orange)"/><path d="M0.5 2 L6 6.5 L11.5 2" fill="none" stroke="var(--white)" stroke-width="1"/></svg>
          <span>john.doe@northmarkresearch.com</span>
        </li>
        <li>
          <svg viewBox="0 0 12 12" aria-hidden="true"><circle cx="6" cy="6" r="5.2" fill="none" stroke="var(--accent-orange)" stroke-width="1.3"/><ellipse cx="6" cy="6" rx="2.2" ry="5.2" fill="none" stroke="var(--accent-orange)" stroke-width="1"/><line x1="0.8" y1="6" x2="11.2" y2="6" stroke="var(--accent-orange)" stroke-width="1"/></svg>
          <span>www.northmarkresearch.com</span>
        </li>
      </ul>
    </div>
  </section>
</main>
</body>
</html>
```